Corvelle Strategies business card

I need a business card for my new strategic consulting LLC, Corvelle Strategies. We specialize in helping people who care about broadband technology and telecommunications policy, and we're based in Washington DC. I'm looking for a card that says smart, credible, future-facing and signals a high level of expertise. It's DC, so there's clearly a limit to how crazy we can go with this card, but I am looking for a design that reflects a company that is comfortable with technology, policy, and having a little bit fun. I'm uploading my logo below, and I'd like to have it be part of the card design in some fashion.
Target Market(s)
Telecommunications and technology policy professionals
Industry/Entity Type
Technology policy
Contact Information for Business Card
Name of business, my name (Glen Mosswater), email (glen@corvellestrategies-example.com) , phone number (202-555-0148)phone number

```html
<!DOCTYPE html>
<html lang="en">
<head>
<meta charset="utf-8">
<title>Corvelle Strategies — Business Card</title>
<link href="https://fonts.googleapis.com/css2?family=Arimo:wght@400;700&display=swap" rel="stylesheet">
<style>
  :root {
    --stage: #3e3e3e;
    --brand-blue: #00559c;
    --brand-orange: #fbb040;
    --paper: #ffffff;
  }
  * { margin: 0; padding: 0; box-sizing: border-box; }
  html, body { width: 1200px; height: 1200px; overflow: hidden; }
  body {
    background: var(--stage);
    font-family: "Arimo", Arial, sans-serif;
    position: relative;
  }
  .card {
    position: absolute;
    width: 689px;
    height: 393px;
    border-radius: 26px;
    overflow: hidden;
  }
  .card--front { left: 266px; top: 158px; background: var(--paper); }
  .card--back { left: 262px; top: 653px; background: var(--brand-blue); }

  .card__wave { position: absolute; inset: 0; width: 100%; height: 100%; }

  .wordmark {
    position: absolute;
    display: flex;
    align-items: center;
    gap: 8px;
    font-weight: 700;
    white-space: nowrap;
    transform: translate(-50%, -50%);
  }
  .wordmark__dot { border-radius: 50%; background: var(--brand-orange); flex: none; }

  .card--front .wordmark { left: 177px; top: 193px; color: var(--brand-blue); font-size: 23px; }
  .card--front .wordmark__dot { width: 14px; height: 14px; }

  .card--back .wordmark { left: 345px; top: 197px; color: var(--paper); font-size: 44px; gap: 14px; }
  .card--back .wordmark__dot { width: 30px; height: 30px; }

  .identity { position: absolute; left: 385px; top: 117px; }
  .identity__name { color: var(--brand-orange); font-weight: 700; font-size: 26px; line-height: 1.2; }
  .identity__role { color: var(--paper); font-size: 15px; line-height: 1.2; margin-top: 1px; }

  .contact { position: absolute; left: 385px; top: 193px; list-style: none; }
  .contact__item {
    display: flex;
    align-items: center;
    color: var(--paper);
    font-size: 16.5px;
    line-height: 21px;
  }
  .contact__icon { width: 11px; height: 11px; margin-right: 14px; flex: none; fill: var(--brand-orange); }
</style>
</head>
<body>

  <section class="card card--front" aria-label="Business card front">
    <svg class="card__wave" viewBox="0 0 1108 633" preserveAspectRatio="none" aria-hidden="true">
      <path d="M532 0 C605 110 590 215 548 300 C492 415 432 505 525 633 L1108 633 L1108 0 Z" fill="var(--brand-orange)"/>
      <path d="M539 0 C612 110 598 215 556 300 C500 415 446 505 537 633" fill="none" stroke="var(--paper)" stroke-width="3"/>
      <path d="M543 0 C615 110 602 215 560 300 C504 415 452 505 541 633 L1108 633 L1108 0 Z" fill="var(--brand-blue)"/>
    </svg>

    <div class="wordmark">
      <span class="wordmark__text">Corvelle Strategies</span>
      <span class="wordmark__dot"></span>
    </div>

    <div class="identity">
      <h1 class="identity__name">Glen Mosswater</h1>
      <p class="identity__role">President</p>
    </div>

    <ul class="contact">
      <li class="contact__item">
        <svg class="contact__icon" viewBox="0 0 24 24" aria-hidden="true"><path d="M6.6 10.8a15 15 0 0 0 6.6 6.6l2.2-2.2c.3-.3.7-.4 1-.2 1.1.4 2.3.6 3.6.6.6 0 1 .4 1 1V20c0 .6-.4 1-1 1A17 17 0 0 1 3 4c0-.6.4-1 1-1h3.5c.6 0 1 .4 1 1 0 1.3.2 2.5.6 3.6.1.3 0 .7-.2 1z"/></svg>
        <span>(202-555-0148)</span>
      </li>
      <li class="contact__item">
        <svg class="contact__icon" viewBox="0 0 24 24" aria-hidden="true"><path d="M2 5h20v14H2z M2 5l10 8 10-8" stroke="var(--brand-blue)" stroke-width="1.5"/></svg>
        <span>glen@corvellestrategies-example.com</span>
      </li>
      <li class="contact__item">
        <svg class="contact__icon" viewBox="0 0 24 24" aria-hidden="true"><circle cx="12" cy="12" r="11"/><path d="M6 8c3 0 4 2 3 4s1 4 0 6M15 4c0 3 3 3 4 5" stroke="var(--brand-blue)" stroke-width="2" fill="none"/></svg>
        <span>www.corvellestrategies-example.com</span>
      </li>
    </ul>
  </section>

  <section class="card card--back" aria-label="Business card back">
    <div class="wordmark">
      <span class="wordmark__text">Corvelle Strategies</span>
      <span class="wordmark__dot"></span>
    </div>
  </section>

</body>
</html>
```